Web Design for Harbor vNet

Need a website for 24/7 online Tv station. Looking for something unique, fresh and different.

When you click on site, I want viewers to automatically see video player. Video player should take up about 70% screen. Still need sections to show thumbnail clicks of our mission - Inspire, Inform and Entertain. Also need section to highlight new shows or events.

This is a family based TV station that will feature Christian content, news, per pay view movies, music videos, sermons from churches. I want site to appeal to 18 -40 year demo graphic. Even though based in California, I also want site appealing enough to all cultures worldwide.

Go to Viewtube and search our channel (harborvnet) for some footages and logo.

Also visit www.harborvnet-example.com to see logo. Need a design that matches logo.

Updates as of 8/28/13:-

http://video.kindlehelpers-example.org/channel/animals-agriculture/
KHTV – like the look and feel. Left side to have 16:9 screen with player and on the right will be still pictures slide show

http://www.zelflix-example.com/?camp=ZeX929&tracking_ID=333914&K_CLICKID=78daa30b-8d66-0e28-e289-000069a1f2b4#home/
ZFX – I like the 16:9 screen (I don’t want mine too big – about 60% of screen)
I want a black background that will also match Harbor vNet red and white logo (see uploaded file)
Updates

KHTV – like the look and feel.  Left side to have 16:9 screen with player and on the right will be still pictures slide show

 

Reason: Need more time for poll results to come in and narrow down to one or two designs.

Target Market(s)

uFone, uSlate generation

I like the look and feel Kindle Helpers TV

Industry/Entity Type

Tv

```html
<!DOCTYPE html>
<html lang="en">
<head>
<meta charset="utf-8">
<title>Harbor vNet</title>
<link href="https://fonts.googleapis.com/css2?family=Arimo:wght@400;700&display=swap" rel="stylesheet">
<style>
:root{
  --bg:#070707;
  --header:#1c1c1c;
  --header-dark:#121212;
  --red:#d8141c;
  --red-dark:#8d0a0f;
  --white:#ffffff;
  --muted:#9a9a9a;
  --panel:#121212;
  --line:#3a3a3a;
  --footer:#2a2a2a;
}
*{box-sizing:border-box;margin:0;padding:0}
html,body{width:1200px;height:926px;overflow:hidden}
body{
  position:relative;
  font-family:"Arimo",Arial,sans-serif;
  color:var(--white);
  background:radial-gradient(ellipse at 50% 40%,#262626 0%,#0d0d0d 55%,var(--bg) 100%);
}
.abs{position:absolute}

/* header */
.site-header{left:0;top:0;width:1200px;height:85px;
  background:linear-gradient(var(--header),var(--header-dark));border-bottom:1px solid #000}
.brand{left:164px;top:22px;font-size:40px;font-weight:700;letter-spacing:-1px;color:var(--white);line-height:40px}
.util-nav a{position:absolute;top:13px;font-size:10.5px;color:var(--white);text-decoration:none}
.main-nav a{position:absolute;top:50px;font-size:12.5px;font-weight:700;color:var(--white);text-decoration:none;letter-spacing:.2px}
.nav-sep{position:absolute;top:49px;width:1px;height:18px;background:#444}
.nav-active{left:562px;top:80px;width:59px;height:3px;background:var(--red)}

/* player */
.player{left:136px;top:113px;width:643px;height:337px;
  background:radial-gradient(ellipse at 50% 50%,#8a8a8a 0%,#3a3a3a 35%,#111 75%),#111;
  box-shadow:0 0 12px #000}
.player-feature{position:absolute;inset:0;
  background:linear-gradient(90deg,rgba(40,90,190,.55) 0%,rgba(0,0,0,0) 30%,rgba(190,170,60,.35) 55%,rgba(0,0,0,0) 75%,rgba(60,170,210,.35) 95%)}
.play-btn{left:304px;top:131px;width:75px;height:75px;border-radius:10px;background:rgba(60,60,60,.75)}
.play-btn span{position:absolute;left:10px;top:10px;width:56px;height:56px;border-radius:8px;background:var(--white)}
.play-btn svg{position:absolute;left:22px;top:17px}
.player-tab{left:300px;top:330px;width:27px;height:7px;background:#2a2a2a;border-radius:2px 2px 0 0}

/* upcoming */
.upcoming{left:803px;top:111px;width:256px;height:338px;background:var(--panel);border:1px solid #333}
.upcoming h2{height:37px;background:linear-gradient(#e0222a,var(--red-dark));font-size:22px;font-weight:700;padding:5px 0 0 11px}
.show{position:absolute;left:12px;width:235px}
.thumb{position:absolute;background:linear-gradient(135deg,#6f5a45,#c8b49a 55%,#5b4a3a);border:1px solid #555}
.duration{position:absolute;right:2px;bottom:2px;background:rgba(0,0,0,.75);font-size:9.5px;font-weight:700;padding:0 2px}
.show h3{position:absolute;left:106px;top:0;font-size:11.5px;font-weight:700;white-space:nowrap}
.show p{position:absolute;left:107px;top:16px;font-size:10.5px;line-height:15px;color:var(--muted);white-space:nowrap}
.view-all{position:absolute;left:0;bottom:0;width:254px;height:31px;background:linear-gradient(#5a5a5a,#2c2c2c);
  font-size:11.5px;font-weight:700;color:#ddd;text-align:right;padding:6px 18px 0 0}

/* mission boxes */
.mission{top:509px;width:279px;height:285px}
.mission-frame{position:absolute;left:0;top:0}
.mission h2{position:absolute;left:10px;top:26px;font-size:19px;font-weight:700}
.item{position:absolute;left:10px;width:245px;height:62px}
.item .thumb{left:0;top:0;width:87px;height:60px}
.thumb.face{background:linear-gradient(135deg,#2a1e17,#8a6a55 60%,#3a2a20)}
.thumb.kitchen{background:linear-gradient(135deg,#5d4a36,#c9b08a 50%,#6b7a4a)}
.thumb.dark{background:linear-gradient(135deg,#0e0a08,#5a3e2e 60%,#120c0a)}
.item h3{position:absolute;left:96px;top:3px;font-size:11.5px;font-weight:700;white-space:nowrap}
.item p{position:absolute;left:97px;top:22px;font-size:10.5px;line-height:14px;color:var(--muted);white-space:nowrap}
.scroll{position:absolute;left:258px;top:60px;width:11px;height:196px;background:#1a1a1a}
.scroll i{position:absolute;left:0;width:11px;background:#9a9a9a}

/* footer */
.site-footer{left:0;top:844px;width:1200px;height:82px;background:linear-gradient(#333,#1f1f1f);border-top:2px solid #444}
.signup-label{left:145px;top:16px;font-size:14.5px;font-weight:700;color:#ddd}
.email{left:143px;top:37px;width:160px;height:22px;background:#0a0a0a;border:1px solid #444;font-size:10px;color:#777;padding:4px}
.go{left:313px;top:37px;width:30px;height:22px;background:linear-gradient(#ddd,#999);border:1px solid #111;color:#111;font-size:13px;font-weight:700;text-align:center;line-height:20px}
.social{top:20px;width:27px;height:27px;border-radius:50%;background:#666}
.footer-brand{left:873px;top:14px;font-size:28px;font-weight:700;letter-spacing:-.5px;color:var(--white)}
.copyright{left:825px;top:58px;font-size:10.5px;color:#aaa}
</style>
</head>
<body>

<header class="site-header abs">
  <div class="brand abs">Harbor vNet</div>
  <nav class="util-nav">
    <a style="left:915px" href="#">Help</a>
    <a style="left:961px" href="#">Login</a>
    <a style="left:1015px" href="#">Sign Up</a>
  </nav>
  <nav class="main-nav">
    <a style="left:568px" href="#">Religion</a>
    <span class="nav-sep" style="left:633px"></span>
    <a style="left:647px" href="#">Entertainment</a>
    <span class="nav-sep" style="left:745px"></span>
    <a style="left:759px" href="#">News</a>
    <span class="nav-sep" style="left:806px"></span>
    <a style="left:821px" href="#">Per Pay View Movies</a>
    <span class="nav-sep" style="left:963px"></span>
    <a style="left:977px" href="#">Music Videos</a>
  </nav>
  <div class="nav-active abs"></div>
</header>

<section class="player abs" role="img" aria-label="Video player showing the station intro title card">
  <div class="player-feature"></div>
  <div class="play-btn abs"><span></span>
    <svg width="34" height="42" viewBox="0 0 34 42"><path d="M12 12 L23 21 L12 30 Z" fill="#111"/></svg>
  </div>
  <div class="player-tab abs"></div>
</section>

<aside class="upcoming abs">
  <h2>Upcoming Shows</h2>
  <div class="show" style="top:50px">
    <div class="thumb" style="left:0;top:0;width:94px;height:57px" role="img" aria-label="Cooking show host in a kitchen"><span class="duration">27:33</span></div>
    <h3>Lorem ipsum dolor sit</h3>
    <p>amet, cons ect et adipisc<br>elit,</p>
  </div>
  <div class="show" style="top:144px">
    <div class="thumb" style="left:0;top:0;width:94px;height:57px" role="img" aria-label="Cooking show host in a kitchen"><span class="duration">27:33</span></div>
    <h3>Lorem ipsum dolor sit</h3>
    <p>amet, cons ect et adipisc<br>elit,</p>
  </div>
  <div class="show" style="top:238px">
    <div class="thumb" style="left:0;top:0;width:94px;height:57px" role="img" aria-label="Cooking show host in a kitchen"><span class="duration">27:33</span></div>
    <h3>Lorem ipsum dolor sit</h3>
    <p>amet, cons ect et adipisc<br>elit,</p>
  </div>
  <div class="view-all">Veiw all videos »</div>
</aside>

<section class="mission abs" style="left:143px">
  <svg class="mission-frame" width="279" height="285" viewBox="0 0 279 285">
    <path d="M0 6 L278 0 L275 6 L0 8 Z" fill="var(--red)"/>
    <rect x="0" y="7" width="275" height="270" fill="#000"/>
    <path d="M0 277 L275 277 L279 285 L2 279 Z" fill="var(--red)"/>
  </svg>
  <h2>INSPIRE</h2>
  <div class="item" style="top:61px"><div class="thumb face" role="img" aria-label="Portrait of a speaker"></div><h3>Lorem ipsum dolor sit</h3><p>Ect etuer adipiscing el Lore<br>ipsu m dolor sit ame conse<br>etuer</p></div>
  <div class="item" style="top:130px"><div class="thumb kitchen" role="img" aria-label="Host preparing food"><span class="duration">18:02</span></div><h3>Duis aute irure dolor</h3><p>Ect etuer adipiscing el Lore<br>ipsu m dolor sit ame conse<br>etuer</p></div>
  <div class="item" style="top:200px"><div class="thumb dark" role="img" aria-label="Person in prayer"></div><h3>Lorem ipsum dolor sit</h3><p>Ect etuer adipiscing el Lore<br>ipsu m dolor sit ame conse<br>etuer</p></div>
  <div class="scroll"><i style="top:0;height:12px"></i><i style="top:47px;height:63px"></i><i style="bottom:0;height:12px"></i></div>
</section>

<section class="mission abs" style="left:461px">
  <svg class="mission-frame" width="279" height="285" viewBox="0 0 279 285">
    <path d="M0 6 L278 0 L275 6 L0 8 Z" fill="var(--red)"/>
    <rect x="0" y="7" width="275" height="270" fill="#000"/>
    <path d="M0 277 L275 277 L279 285 L2 279 Z" fill="var(--red)"/>
  </svg>
  <h2>INFORM</h2>
  <div class="item" style="top:61px"><div class="thumb face" role="img" aria-label="Portrait of a speaker"></div><h3>Lorem ipsum dolor sit</h3><p>Ect etuer adipiscing el Lore<br>ipsu m dolor sit ame conse<br>etuer</p></div>
  <div class="item" style="top:130px"><div class="thumb kitchen" role="img" aria-label="Host preparing food"><span class="duration">18:02</span></div><h3>Duis aute irure dolor</h3><p>Ect etuer adipiscing el Lore<br>ipsu m dolor sit ame conse<br>etuer</p></div>
  <div class="item" style="top:200px"><div class="thumb dark" role="img" aria-label="Person in prayer"></div><h3>Lorem ipsum dolor sit</h3><p>Ect etuer adipiscing el Lore<br>ipsu m dolor sit ame conse<br>etuer</p></div>
  <div class="scroll"><i style="top:0;height:12px"></i><i style="top:47px;height:63px"></i><i style="bottom:0;height:12px"></i></div>
</section>

<section class="mission abs" style="left:780px">
  <svg class="mission-frame" width="279" height="285" viewBox="0 0 279 285">
    <path d="M0 6 L278 0 L275 6 L0 8 Z" fill="var(--red)"/>
    <rect x="0" y="7" width="275" height="270" fill="#000"/>
    <path d="M0 277 L275 277 L279 285 L2 279 Z" fill="var(--red)"/>
  </svg>
  <h2>ENTERTAIN</h2>
  <div class="item" style="top:61px"><div class="thumb face" role="img" aria-label="Portrait of a speaker"></div><h3>Lorem ipsum dolor sit</h3><p>Ect etuer adipiscing el Lore<br>ipsu m dolor sit ame conse<br>etuer</p></div>
  <div class="item" style="top:130px"><div class="thumb kitchen" role="img" aria-label="Host preparing food"><span class="duration">18:02</span></div><h3>Duis aute irure dolor</h3><p>Ect etuer adipiscing el Lore<br>ipsu m dolor sit ame conse<br>etuer</p></div>
  <div class="item" style="top:200px"><div class="thumb dark" role="img" aria-label="Person in prayer"></div><h3>Lorem ipsum dolor sit</h3><p>Ect etuer adipiscing el Lore<br>ipsu m dolor sit ame conse<br>etuer</p></div>
  <div class="scroll"><i style="top:0;height:12px"></i><i style="top:47px;height:63px"></i><i style="bottom:0;height:12px"></i></div>
</section>

<footer class="site-footer abs">
  <div class="signup-label abs">Newsletter signup</div>
  <div class="email abs">email here</div>
  <div class="go abs">GO</div>
  <span class="social abs" style="left:715px" aria-label="Social link"></span>
  <span class="social abs" style="left:752px" aria-label="Social link"></span>
  <span class="social abs" style="left:789px" aria-label="Social link"></span>
  <div class="footer-brand abs">Harbor vNet</div>
  <div class="copyright abs">Copyright © 2013  Harborvnet. All Rights Reserved.</div>
</footer>

</body>
</html>
```